"You CAN Relax on Your Own Savings!" book cover for 80 page or so book.

Need a book cover that stands out on Bookvale, so highly engaging colors, need to reflect optimism, hope and determination. Go to Bookvale, type my name in and see the covers for the three other books I had written.

There's a lot of negativity and fear for Americans looking at retirement. Yet, they don't need that fear, my book tells them why they can be confident in their ability to retire.

There will be NO spine writing for the book, too small.

Target Market(s)

stressed out people in their 50s and 60s. This book appeals to working people, not high end, wealthy types.

Industry/Entity Type

Financial Planning

Colors

Designer to choose colors to be used in the design.

Requirements
Must have
• Needs to reflect simplicity in action.
• Please spell out my full name, GREG MALTHORPE, at the bottom of the cover.
Nice to have
• if there is anyway to put a picture of an RV (Recreational Vehicle) that would be great.
Should not have
• Do NOT want to be the stodgy, typical financial planning literature out there. No guy in a suit and tie. No one sitting on a beach.
• Do not want my face on the cover either. (On the back yes.)

```html
<!DOCTYPE html>
<html lang="en">
<head>
<meta charset="utf-8">
<title>You CAN Relax on Your Own Savings – Book Cover</title>
<link href="https://fonts.googleapis.com/css2?family=Oswald:wght@400;500;600;700&family=Jost:wght@500;600&display=swap" rel="stylesheet">
<style>
  :root {
    --stage: #121212;
    --paper: #f0f0f0;
    --green: #17763a;
    --ink: #2a2a2a;
    --frame: #333333;
  }
  * { margin: 0; padding: 0; box-sizing: border-box; }
  html, body { width: 1200px; height: 854px; overflow: hidden; background: var(--stage); }
  .canvas { position: relative; width: 1200px; height: 854px; }
  .jacket {
    position: absolute; left: 186px; top: 114px; width: 854px; height: 629px;
    background: var(--paper);
  }
  .back { position: absolute; left: 0; top: 0; width: 427px; height: 629px; }
  .back-title { position: absolute; left: 59px; top: 44px; width: 130px; font-family: 'Oswald', sans-serif; color: var(--green); }
  .back-title .line1 { display: flex; align-items: baseline; justify-content: flex-end; white-space: nowrap; line-height: 1; }
  .back-title .you { font-size: 17px; font-weight: 500; }
  .back-title .can { font-size: 31px; font-weight: 700; margin: 0 2px; }
  .back-title .relax { font-size: 20px; font-weight: 400; }
  .back-title .line2 { text-align: right; color: var(--ink); font-size: 14px; font-weight: 600; letter-spacing: .3px; margin-top: 5px; white-space: nowrap; }
  .back-title .line2 .on { font-size: 9px; font-weight: 400; }
  .benefits { position: absolute; left: 75px; top: 122px; list-style: none; font-family: 'Jost', sans-serif; font-weight: 500; font-size: 11.5px; line-height: 14.8px; color: var(--ink); }
  .benefits li::before { content: "• "; }
  .back-url { position: absolute; left: 0; width: 427px; top: 195px; text-align: center; font-family: 'Jost', sans-serif; font-weight: 600; font-size: 13px; color: var(--ink); padding-left: 10px; }
  .back-rule { position: absolute; left: 52px; top: 230px; width: 315px; height: 3px; background: var(--ink); }
  .author-photo { position: absolute; left: 79px; top: 244px; width: 101px; height: 152px; background: linear-gradient(180deg, #8a8f86 0%, #6c6f70 45%, #77797b 100%); }
  .firm-mark { position: absolute; left: 76px; top: 441px; width: 107px; height: 59px; background: #ffffff; display: flex; align-items: center; justify-content: center; gap: 5px; font-family: 'Jost', sans-serif; font-weight: 500; font-size: 9.5px; color: #3d8aa0; letter-spacing: .5px; }
  .firm-mark .dot { width: 10px; height: 10px; border-radius: 50%; background: #3d8aa0; }
  .bio { position: absolute; left: 193px; top: 244px; width: 160px; font-family: 'Jost', sans-serif; font-weight: 500; font-size: 10px; line-height: 12.8px; color: #1e1e1e; }
  .bio p + p { margin-top: 13px; }
  .bio .lead { text-align: center; }

  .front { position: absolute; left: 440px; top: 6px; width: 407px; height: 617px; border: 2px solid var(--frame);
    background: radial-gradient(ellipse at 50% 70%, #f7f7f7 0%, #eeeeee 55%, #e6e6e6 100%); }
  .front-title { position: absolute; left: 16px; top: 132px; width: 366px; font-family: 'Oswald', sans-serif; color: var(--green); }
  .front-title .line1 { display: flex; align-items: baseline; justify-content: space-between; line-height: 1; border-bottom: 3px solid var(--green); padding-bottom: 2px; }
  .front-title .you { font-size: 44px; font-weight: 500; }
  .front-title .can { font-size: 88px; font-weight: 700; letter-spacing: -1px; }
  .front-title .relax { font-size: 54px; font-weight: 400; }
  .front-title .line2 { text-align: right; color: var(--ink); font-size: 34px; font-weight: 600; letter-spacing: 1px; margin-top: 4px; white-space: nowrap; }
  .front-title .line2 .on { font-size: 23px; font-weight: 500; }
  .vehicle-art { position: absolute; left: 80px; top: 330px; width: 240px; height: 125px; border-radius: 26px 18px 10px 10px;
    background: radial-gradient(ellipse at 50% 45%, #fafafa 0%, #d9d9d9 60%, rgba(230,230,230,0) 100%); }
  .author-name { position: absolute; left: 0; width: 403px; top: 512px; text-align: center; font-family: 'Oswald', sans-serif; font-weight: 500; font-size: 36px; line-height: 1; color: var(--green); letter-spacing: .5px; }
  .front-url { position: absolute; left: 0; width: 403px; top: 556px; text-align: center; font-family: 'Oswald', sans-serif; font-weight: 500; font-size: 13px; color: var(--green); }
  .front-url span { border-bottom: 2px solid var(--green); padding-bottom: 1px; }
</style>
</head>
<body>
<div class="canvas">
  <div class="jacket">
    <section class="back">
      <div class="back-title">
        <div class="line1"><span class="you">You</span><span class="can">CAN</span><span class="relax">RELAX</span></div>
        <div class="line2"><span class="on">on </span>YOUR OWN SAVINGS</div>
      </div>
      <ul class="benefits">
        <li>REDUCE income taxes</li>
        <li>ELIMINATE Social Security taxes</li>
        <li>AVOID huge Medicare premium increases</li>
        <li>LEAVE a tax-free legacy</li>
      </ul>
      <div class="back-url">www.harborlinefinancial.com</div>
      <div class="back-rule"></div>
      <div class="author-photo" role="img" aria-label="Portrait photo of the author standing on a street"></div>
      <div class="firm-mark"><span class="dot"></span>HARBORLINE</div>
      <div class="bio">
        <p class="lead">Greg Malthorpe is a CERTIFIED FINANCIAL PLANNER and holds a Master’s degree in Personal Financial Planning.</p>
        <p>Greg has provided financial advice to clients since 1998. Over those 2 decades he has developed extensive knowledge of investment management, Social Security, tax, retirement planning and wealth transfer strategies.</p>
        <p>He has learned that successful financial planning does not need to be complex. He follows the tried and true rule he learned in the Army, “Keep It Simple, Stupid”</p>
      </div>
    </section>
    <section class="front">
      <div class="front-title">
        <div class="line1"><span class="you">You</span><span class="can">CAN</span><span class="relax">RELAX</span></div>
        <div class="line2"><span class="on">on </span>YOUR OWN SAVINGS</div>
      </div>
      <div class="vehicle-art" role="img" aria-label="Photo of a small white toy camper van"></div>
      <div class="author-name">GREG MALTHORPE</div>
      <div class="front-url"><span>www.harborlinefinancial.com</span></div>
    </section>
  </div>
</div>
</body>
</html>
```